International Trading Company, 'KIRO' needs a Business Card

The company name is "KIRO" and it has own logo design.
I'd like to use its logo on this business card.
I need two side Business Card.
I'll look forward to your great design.
Thank you very much in advance.

Contact Information for Business Card

Company Name : Kiro Harbour Limited
Information Example
Dorian Pallister
Mobile(use icon please) : 1 (212) 555-0143
Tel(use icon please) : 1 (212) 555-0178
Email(use icon please) : dorian27@kiroharbour-mail.com
Address(use icon please) : 482 Halden Ave, New York, NY 10160, USA

```html
<!DOCTYPE html>
<html lang="en">
<head>
<meta charset="utf-8">
<title>Kiro Harbour Limited – Business Card</title>
<link href="https://fonts.googleapis.com/css2?family=PT+Sans:wght@400;700&display=swap" rel="stylesheet">
<style>
  :root {
    --backdrop: #c9c9c9;
    --card: #000000;
    --logo-grey: #5e5e60;
    --name-grey: #c4c4c4;
    --tile: #58585a;
    --icon: #c9c9c9;
    --tile-text: #d2d2d2;
  }
  * { margin: 0; padding: 0; box-sizing: border-box; }
  html, body { width: 1000px; height: 1200px; overflow: hidden; }
  body {
    background: var(--backdrop);
    font-family: "PT Sans", sans-serif;
    position: relative;
  }
  .card { position: absolute; background: var(--card); }
  .card-front { left: 74px; top: 30px; width: 828px; height: 518px; }
  .card-back { left: 78px; top: 610px; width: 822px; height: 530px; }

  .brand-name {
    position: absolute; left: 0; right: 0; top: 128px;
    text-align: center;
    font-size: 138px; font-weight: 700; line-height: 1;
    letter-spacing: 6px;
    color: var(--logo-grey);
  }
  .company-name {
    position: absolute; left: 0; right: 0; top: 287px;
    text-align: center;
    font-size: 25px; font-weight: 400;
    letter-spacing: 12px;
    color: var(--logo-grey);
    text-transform: uppercase;
  }
  .person-name {
    position: absolute; left: 0; right: 0; top: 438px;
    text-align: center;
    font-size: 27px;
    color: var(--name-grey);
    text-transform: uppercase;
  }
  .person-name .first { font-weight: 400; }
  .person-name .last { font-weight: 700; }

  .tile {
    position: absolute; width: 354px; height: 210px;
    background: var(--tile);
    display: flex; flex-direction: column; align-items: center;
    color: var(--tile-text);
    text-align: center;
  }
  .tile-mobile { left: 38px; top: 36px; }
  .tile-phone { left: 430px; top: 36px; }
  .tile-email { left: 38px; top: 282px; }
  .tile-address { left: 430px; top: 282px; }
  .tile svg { display: block; fill: var(--icon); }
  .tile-mobile svg, .tile-phone svg { margin-top: 36px; height: 94px; }
  .tile-email svg { margin-top: 42px; height: 90px; }
  .tile-address svg { margin-top: 30px; height: 84px; }
  .contact-text { font-size: 25px; line-height: 1.25; margin-top: 42px; }
  .tile-email .contact-text { font-size: 21px; margin-top: 40px; }
  .tile-address .contact-text { margin-top: 14px; }
</style>
</head>
<body>
  <section class="card card-front">
    <div class="brand-name">KIRO</div>
    <div class="company-name">Kiro Harbour Limited</div>
    <div class="person-name"><span class="first">Dorian</span> <span class="last">Pallister</span></div>
  </section>

  <section class="card card-back">
    <div class="tile tile-mobile">
      <svg viewBox="0 0 54 94" width="54" aria-label="Mobile">
        <path d="M6 0h42a6 6 0 0 1 6 6v82a6 6 0 0 1-6 6H6a6 6 0 0 1-6-6V6a6 6 0 0 1 6-6zM5 10v66h44V10zM20 3.5v2.5h14V3.5z"/>
        <circle cx="27" cy="85" r="4" fill="var(--tile)"/>
      </svg>
      <div class="contact-text">1 (212) 555-0143</div>
    </div>

    <div class="tile tile-phone">
      <svg viewBox="0 0 70 94" width="70" aria-label="Telephone">
        <path d="M46 2c6-3 12-2 16 3 9 12 8 40-6 60C43 84 22 95 9 92c-6-1-9-6-8-11l2-4c1-3 4-4 7-3l16 5c3 1 6 0 8-3l2-3c1-2 0-4-2-5l-8-4c14-10 23-27 24-44l-9-2c-2 0-3-2-3-4l1-9c1-3 3-5 7-6z"/>
      </svg>
      <div class="contact-text">1 (212) 555-0178</div>
    </div>

    <div class="tile tile-email">
      <svg viewBox="0 0 120 90" width="120" aria-label="Email">
        <path d="M0 32h96v58H0zM0 32l48 34 48-34v8L48 74 0 40z" />
        <path d="M0 32l48 34 48-34" fill="none" stroke="var(--tile)" stroke-width="4"/>
        <circle cx="94" cy="26" r="26"/>
        <circle cx="94" cy="26" r="20" fill="var(--tile)"/>
        <text x="94" y="36" text-anchor="middle" font-family="PT Sans, sans-serif" font-weight="700" font-size="30" fill="var(--icon)">@</text>
      </svg>
      <div class="contact-text">dorian27@kiroharbour-mail.com</div>
    </div>

    <div class="tile tile-address">
      <svg viewBox="0 0 52 84" width="52" aria-label="Location">
        <path d="M26 0a26 26 0 0 1 26 26c0 14-12 24-26 58C12 50 0 40 0 26A26 26 0 0 1 26 0z"/>
        <circle cx="26" cy="25" r="9" fill="var(--tile)"/>
      </svg>
      <div class="contact-text">482 Halden Ave, New York,<br>NY 10160, USA</div>
    </div>
  </section>
</body>
</html>
```